Re-design my 1-page website to be BETTER!

Hi Guys,
I recently created a 1-page website for market testing purposes for a company I am starting. Problem is, the feedback i've had on the page is its a bit corporate and boring.
I would love you to design something that is fresher, more modern and will generate leads (via the sign up CTA's).
Here is the website as it is now: www.guidelinkhub.com.au.
If you need any info or have questions, just reach out.
Thanks,
Oliver

Target Market(s)

Entrepreneurs

Number of Pages Required

1 page

Font styles to use
Sans Serif

Colors
abd036
34a6d7
ffffff

Requirements
Must have
• Fresh, Modern, high-converting
• I expect 70% of traffic to be mobile so must be mobile optimised first.
Nice to have
• I've highlighted colours i like below, however, I am open to suggestions. I like colours that are gender neutral and show energy and vibrancy.
• I have used Proxima Nova for the fonts, as I find it easy to read however, I am open to suggestions. My main preference is that it displays well and is easily read

```html
<!DOCTYPE html>
<html lang="en">
<head>
<meta charset="utf-8">
<title>GuideLink Hub – A Mentor for Everyone</title>
<link rel="stylesheet" href="https://fonts.googleapis.com/css2?family=Montserrat:wght@400;500;600;700;800&display=swap">
<style>
:root{
  --blue:#34a6d7;
  --blue-dark:#2388b6;
  --green:#abd036;
  --coral:#f26b5b;
  --coral-dark:#e85a49;
  --ink:#333a40;
  --muted:#7a8288;
  --light:#f4f6f7;
  --white:#ffffff;
  --night:#262a2e;
}
*{box-sizing:border-box;margin:0;padding:0}
html,body{width:1200px;height:3448px;overflow:hidden}
body{font-family:"Montserrat",sans-serif;color:var(--ink);background:var(--white)}
section,header,footer{position:relative;width:1200px;overflow:hidden}
.btn{display:inline-block;font-weight:600;letter-spacing:1px;text-transform:uppercase;border-radius:40px;font-size:18px;padding:16px 44px}
.btn-ghost{border:2px solid var(--white);color:var(--white)}

/* Hero */
.hero{height:440px;background:linear-gradient(120deg,#3d4c58 0%,#5d6b75 40%,#8b6d5e 75%,#4a4f55 100%);color:var(--white);text-align:center}
.hero-photo{position:absolute;inset:0;background:linear-gradient(120deg,rgba(30,40,50,.55),rgba(90,70,60,.35))}
.nav{position:absolute;top:10px;left:0;right:0;display:flex;justify-content:center;gap:48px;font-size:16px;font-weight:500;align-items:center}
.nav .socials{display:flex;gap:10px;margin-left:10px}
.dot{width:26px;height:26px;border-radius:50%;background:var(--white);opacity:.9}
.brand{position:absolute;top:100px;left:0;right:0}
.brand-name{font-size:54px;font-weight:700;color:var(--green)}
.brand-tag{font-size:20px;letter-spacing:4px;font-weight:500;margin-top:2px}
.quote{position:absolute;top:200px;left:270px;width:660px;font-size:16px;line-height:1.5;font-style:italic}
.hero .btn{position:absolute;top:325px;left:50%;transform:translateX(-50%);font-size:17px;padding:12px 38px}
.hero-band{position:absolute;bottom:0;left:0}
.band-text{position:absolute;bottom:22px;left:0;right:0;font-size:13px;color:var(--white);font-weight:500}

/* Intro */
.intro{height:480px;padding-top:60px}
.intro-photo{position:absolute;left:130px;top:80px;width:400px;height:290px;background:linear-gradient(135deg,#c9b7a3,#8e7a66 55%,#4f5d66);border-radius:4px}
.intro-copy{position:absolute;left:580px;top:70px;width:470px}
.intro-copy h2{font-size:24px;font-weight:700;margin-bottom:18px}
.intro-copy p{font-size:14px;line-height:1.6;color:var(--muted);margin-bottom:6px}
.btn-blue{background:var(--blue);color:var(--white);border-radius:4px;text-transform:none;letter-spacing:0;font-size:20px;padding:14px 36px;margin-top:18px}
.intro-copy .btn-blue{margin-left:110px}

/* Mentorship */
.different{height:610px}
.ribbon{margin:0 140px;background:var(--coral);color:var(--white);text-align:center;font-size:28px;font-weight:700;padding:12px 0}
.different .sub{text-align:center;font-size:13px;color:var(--muted);margin-top:16px}
.different .sub a{color:var(--blue)}
.cards{display:flex;gap:36px;justify-content:center;margin-top:22px}
.card{width:300px;height:330px;border:1px solid #dfe3e5;background:var(--white)}
.card-head{background:var(--green);color:var(--white);font-weight:700;font-size:17px;padding:8px 12px}
.card-img{height:140px;margin:12px 14px;background:linear-gradient(135deg,#7d9aa8,#c3cfd6 60%,#8e9ba1)}
.card p{font-size:13px;line-height:1.5;color:var(--muted);text-align:center;padding:0 18px}
.btn-outline{display:block;width:310px;margin:42px auto 0;border:2px solid var(--blue);color:var(--ink);text-align:center;border-radius:40px;font-size:22px;padding:12px 0;font-weight:500}
.different .note{text-align:center;color:var(--muted);font-size:15px;margin-top:14px}

/* Growth */
.growth{height:840px;background:var(--coral);color:var(--white)}
.growth h2{text-align:center;font-size:30px;font-weight:700;padding-top:64px}
.points{position:absolute;top:180px;left:150px;width:900px;display:grid;grid-template-columns:1fr 1fr;column-gap:180px;row-gap:50px}
.point{display:flex;gap:22px}
.num{font-size:32px;font-weight:700;line-height:1}
.point h3{font-size:18px;font-weight:700;margin-bottom:8px}
.point p{font-size:13px;line-height:1.55;opacity:.92}
.growth .btn{position:absolute;top:690px;left:50%;transform:translateX(-50%);font-size:22px;padding:12px 44px}
.growth .foot{position:absolute;top:770px;left:0;right:0;text-align:center;font-size:13px;opacity:.9}

/* FAQ */
.faq{height:570px;background:var(--white)}
.faq h2{text-align:center;font-size:26px;font-weight:600;padding-top:42px;margin-bottom:28px}
.faq-list{width:640px;margin:0 auto}
.q{background:#8fcbe9;color:var(--white);border-radius:8px;font-size:15px;padding:10px 18px;margin-bottom:14px;display:flex;justify-content:space-between}
.q.open{background:var(--blue);flex-direction:column}
.q.open .q-row{display:flex;justify-content:space-between}
.q.open p{font-size:12px;line-height:1.5;margin-top:8px;opacity:.95}

/* Invest */
.invest{height:340px;background:linear-gradient(135deg,#2c2f35 0%,#3c2f3a 45%,#b04a6c 100%);color:var(--white);text-align:center}
.invest-shade{position:absolute;inset:0;background:rgba(20,22,26,.45)}
.invest-inner{position:relative;padding-top:44px}
.invest h2{font-size:30px;font-weight:700}
.invest p{width:780px;margin:22px auto 0;font-size:14px;line-height:1.55}
.invest p.accent{color:var(--green);margin-top:6px}
.invest .btn{margin-top:26px;font-size:22px;padding:12px 44px}

/* Footer */
.site-footer{height:128px;background:var(--night);display:flex;justify-content:center;align-items:center;gap:56px}
.site-footer .dot{width:44px;height:44px;background:#dcdfe1}
</style>
</head>
<body>

<header class="hero">
  <div class="hero-photo" role="img" aria-label="Photo of a team collaborating over sticky notes on a glass wall"></div>
  <nav class="nav">
    <span>Home</span><span>About</span><span>F.A.Q</span>
    <span class="socials"><span class="dot"></span><span class="dot"></span><span class="dot"></span><span class="dot"></span></span>
  </nav>
  <div class="brand">
    <div class="brand-name">GuideLink Hub</div>
    <div class="brand-tag">A MENTOR FOR EVERYONE</div>
  </div>
  <p class="quote">"We've flipped the model on its head – so now you choose your Mentor, it's never been this easy to get the advice and guidance you need to thrive" Oliver, Founder – GuideLink Hub</p>
  <span class="btn btn-ghost">Find My Mentor</span>
  <svg class="hero-band" width="1200" height="90" viewBox="0 0 1200 90" aria-hidden="true">
    <polygon points="0,30 600,60 1200,0 1200,90 0,90" fill="var(--blue)"/>
    <polygon points="0,84 600,70 1200,84 1200,90 0,90" fill="var(--white)"/>
  </svg>
  <div class="band-text">Low Registration, 100% Confidential, 100% Obligation Free</div>
</header>

<section class="intro">
  <div class="intro-photo" role="img" aria-label="Photo of a circle of hands stacked together"></div>
  <div class="intro-copy">
    <h2>Finding a Mentor Has Never Been Easier</h2>
    <p>Having a great Mentor will turbo charge your personal, professional or business growth. But unless you have an incredible network, finding great Mentors has always been a challenge.</p>
    <p>GuideLink Hub changes all that, levelling the playing field and making it easy for entrepreneurs and professionals to find the advice and guidance they deserve.</p>
    <p>No longer will you have to go searching for your perfect Mentor. We bring the perfect Mentor to you, selected from a global pool of experts, putting the power back in your hands and letting you get on with your growth.</p>
    <span class="btn btn-blue">Let's Get Started</span>
  </div>
</section>

<section class="different">
  <div class="ribbon">Mentorship: But Different</div>
  <p class="sub">Finding a Mentor used to be hard, but not any more. We've turned the traditional model on its head, so now <a>Mentors apply to you</a>.</p>
  <div class="cards">
    <div class="card">
      <div class="card-head">1. Tell Us What You Need</div>
      <div class="card-img" role="img" aria-label="Photo of a person writing notes at a desk"></div>
      <p>There is no one size fits all approach to Mentorship. So tell us the challenges you are facing and the Mentor your ideal match looks like.</p>
    </div>
    <div class="card">
      <div class="card-head">2. Choose Your Mentor</div>
      <div class="card-img" role="img" aria-label="Photo of two people shaking hands"></div>
      <p>Mentors are invited to Mentor you, the select it has who align with your needs. It's then up to you whether you choose a Mentor, connect or if none of them suit, you start again.</p>
    </div>
    <div class="card">
      <div class="card-head">3. Ongoing Support</div>
      <div class="card-img" role="img" aria-label="Photo of people meeting around a table"></div>
      <p>We don't stop once you have your perfect Mentor. We're on hand to check in with you, keep your sessions on track and provide ongoing support.</p>
    </div>
  </div>
  <span class="btn-outline">REGISTER FOR FREE</span>
  <p class="note">100% confidential and 100% obligation free</p>
</section>

<section class="growth">
  <h2>How a Mentor Will Accelerate Your Growth</h2>
  <div class="points">
    <div class="point"><span class="num">1.</span><div><h3>Impartial advice</h3><p>Friends, family and colleagues mean well, but their advice is coloured by how they know you. A Mentor offers honest, independent guidance based purely on what is best for you and your goals.</p></div></div>
    <div class="point"><span class="num">4.</span><div><h3>Clarity</h3><p>Sometimes we are so caught up in our own world we struggle to see the big picture. Your Mentor helps you step back, find perspective and focus your energy on what matters.</p></div></div>
    <div class="point"><span class="num">2.</span><div><h3>Avoid the Pitfalls</h3><p>An experienced Mentor will help you spot the roadblocks before they arrive and avoid the mistakes others made, saving you time, stress and money on your journey.</p></div></div>
    <div class="point"><span class="num">5.</span><div><h3>Motivation</h3><p>Your Mentor has been there before and will push you further. They understand the highs and lows and will keep you fired up when things get tough.</p></div></div>
    <div class="point"><span class="num">3.</span><div><h3>A Supportive Ear</h3><p>Running a business can be lonely. Your Mentor is someone to talk things through with openly, who listens without judgement and wants to see you succeed.</p></div></div>
    <div class="point"><span class="num">6.</span><div><h3>Makes you Accountable</h3><p>Your Mentor will hold you to the goals you set together, keeping you moving forward and making sure real progress happens between every session.</p></div></div>
  </div>
  <span class="btn btn-ghost">Register Now</span>
  <p class="foot">Your chance to your perfect mentor than you think. Register today to see how easy it can be.</p>
</section>

<section class="faq">
  <h2>Frequently Asked Questions</h2>
  <div class="faq-list">
    <div class="q"><span>What is a Mentor?</span><span>+</span></div>
    <div class="q open">
      <div class="q-row"><span>Is a Mentor right for me?</span><span>–</span></div>
      <p>If you have a desire to achieve a challenging or ambitious goal, then a Mentor can help you get there faster. Whether you are starting out, growing a business or stepping into a new role, a Mentor brings the experience and perspective to guide you. If you're not sure, register for free and see who applies to help.</p>
    </div>
    <div class="q"><span>How often do we meet?</span><span>+</span></div>
    <div class="q"><span>Can I book more than one Mentor?</span><span>+</span></div>
    <div class="q"><span>What if it doesn't work out?</span><span>+</span></div>
    <div class="q"><span>How do we meet?</span><span>+</span></div>
    <div class="q"><span>How do we start?</span><span>+</span></div>
  </div>
</section>

<section class="invest">
  <div class="invest-shade" role="img" aria-label="Photo of a city skyline at dusk in pink and dark tones"></div>
  <div class="invest-inner">
    <h2>It's Time to Invest in You</h2>
    <p>If you've come this far you've already taken the first step. Take the next one now and register to find the perfect Mentor who will help you reach your goals faster than you ever imagined.</p>
    <p class="accent">Get started for free today. No obligation. Connect the dots now.</p>
    <span class="btn btn-ghost">Let's Do This</span>
  </div>
</section>

<footer class="site-footer">
  <span class="dot"></span><span class="dot"></span><span class="dot"></span><span class="dot"></span>
</footer>

</body>
</html>
```